Business Card Design- Mortgage Firm

Looking to design a business Card for our Outside sales people. This card is used to provide their contact information to prospective clients and realtors. Must have All Pertinent company and licensing information by law. We are looking for a very modern design that flows with our current logo color scheme. Red/White/Black

Industry/Entity Type

Mortgage Lender

Contact Information for Business Card

Must stick with current color scheme.

Colors
f04a50
ffffff
ecf7fb

Requirements
Must have
• Company Logo or similar
• Company Address (547 W Larkin Avenue, Suite 318, Brookvale CA 92877 NMLS: 2947163)
• Agent Name (Nora Pell)
• Title (Senior Mortgage Loan Originator)
• NMLS# 7395281
• Toll Free: 800-627-3184
• Direct : 310-555-8347
Nice to have
• Room for Agent Picture

```html
<!DOCTYPE html>
<html lang="en">
<head>
<meta charset="utf-8">
<title>Meridell Mortgage – Business Card</title>
<link rel="stylesheet" href="https://fonts.googleapis.com/css2?family=PT+Sans:wght@400;700&display=swap">
<style>
  :root {
    --brand-red: #b81f27;
    --ink: #3a3a3a;
    --ink-soft: #4a4a4a;
    --card: #ffffff;
    --ring: #d4d6d8;
    --portrait-light: #7b858d;
    --portrait-dark: #3f474e;
    --backdrop: #e6e6e6;
  }
  * { margin: 0; padding: 0; box-sizing: border-box; }
  html, body {
    width: 1200px; height: 801px; overflow: hidden;
    background: var(--backdrop);
    font-family: "PT Sans", Arial, sans-serif;
  }
  .card {
    position: absolute; left: 40px; top: 80px;
    width: 1120px; height: 641px;
    background: var(--card);
    box-shadow: 0 2px 10px rgba(0,0,0,.18);
    overflow: hidden;
  }
  .brand { position: absolute; left: 50px; top: 86px; display: flex; align-items: center; gap: 22px; }
  .brand-square { width: 96px; height: 96px; background: var(--brand-red); }
  .brand-name {
    color: var(--brand-red); font-weight: 700; font-size: 46px;
    line-height: 1.05; letter-spacing: 4px; text-transform: uppercase;
  }
  .address {
    position: absolute; left: 58px; top: 294px;
    color: var(--ink); font-size: 30px; line-height: 49px;
  }
  .phones {
    position: absolute; left: 58px; top: 410px;
    color: var(--ink); font-size: 30px; line-height: 45px;
  }
  .phones .label { color: var(--brand-red); font-weight: 700; }
  .license-band { position: absolute; left: 0; top: 530px; width: 520px; height: 65px; }
  .license-band svg { position: absolute; inset: 0; }
  .license-band span {
    position: relative; display: block; padding-left: 58px;
    line-height: 65px; color: #fff; font-weight: 700; font-size: 30px; letter-spacing: .5px;
  }
  .portrait {
    position: absolute; left: 629px; top: 79px;
    width: 424px; height: 424px; border-radius: 50%;
    border: 10px solid var(--ring);
    background: radial-gradient(circle at 50% 40%, var(--portrait-light), var(--portrait-dark));
  }
  .agent {
    position: absolute; left: 629px; width: 440px; top: 510px;
    text-align: center;
  }
  .agent-name { color: var(--brand-red); font-weight: 700; font-size: 50px; line-height: 56px; }
  .agent-title { color: var(--ink-soft); font-size: 22px; line-height: 30px; margin-top: 8px; letter-spacing: .3px; }
</style>
</head>
<body>
  <main class="card">
    <div class="brand">
      <div class="brand-square"></div>
      <div class="brand-name">Meridell<br>Mortgage</div>
    </div>

    <div class="address">
      <p>547 W Larkin Avenue, Suite 318</p>
      <p>Brookvale CA 92877, NMLS: 2947163</p>
    </div>

    <div class="phones">
      <p><span class="label">Toll Free:</span> 800-627-3184</p>
      <p><span class="label">Direct :</span> 310-555-8347</p>
    </div>

    <div class="license-band">
      <svg width="520" height="65" viewBox="0 0 520 65" aria-hidden="true">
        <polygon points="0,0 518,0 473,65 0,65" fill="var(--brand-red)"/>
      </svg>
      <span>NMLS# 7395281</span>
    </div>

    <div class="portrait" role="img" aria-label="Agent portrait photo"></div>

    <div class="agent">
      <p class="agent-name">Nora Pell</p>
      <p class="agent-title">SENIOR MORTGAGE LOAN ORIGINATOR</p>
    </div>
  </main>
</body>
</html>
```